Indian Wedding Invitation

Hello Designers,

We are looking for a fantastic graphic designer to help us come up with our very own bespoke wedding invitation.

We have a logo which we would like to use (see attached) and a very good idea of the style of invitation we are after.

Specification:

- We would like the wedding invitation to be A5 (landscape) with a pocket within it to allow for 3 inserts.
- The pocket should be at the bottom when you open up the card
- The first insert will be A5, the second will be slightly smaller and then the final one will be slightly smaller than that (so that you can see that there are 3 invites included in the invite) - see attached images for what I am referring to
- We will need all 3 of these to match the design of the card
- Once you open the card, the top of the card will contain some content - like details of where we are getting married / timings / rsvp information etc.
- Content will be provided once we have a view of the design

See attached images for the type of designs we are looking for. Also see: http://www.lorvanpress.co.uk/pocket-fold-invitations.html

We are looking for a fresh approach to this card.

We do not have any preference on colour, but it should work well with the logo design that we have.

Hope this is enough information to get you started. Any questions, please drop me a message or email me on tkelmore@fenwickpost.com. I'm usually very quick at responding.

Thanks!

Industry/Entity Type

Graphic Designer

Requirements
Must have
• Classy and high-end look and feel

Use of subtle colours - nothing bright

```html
<!DOCTYPE html>
<html lang="en">
<head>
<meta charset="utf-8">
<title>Wedding Invitation</title>
<link href="https://fonts.googleapis.com/css2?family=Playball&display=swap" rel="stylesheet">
<style>
  :root {
    --stage: #353535;
    --cream: #f2e4ca;
    --damask: #f0d3cc;
    --gold: #c9952f;
    --magenta: #f36ce8;
    --blush: #f7aaf5;
    --plum: #5e1f63;
    --glow: #ffffff;
  }
  html, body {
    margin: 0;
    width: 1200px;
    height: 900px;
    overflow: hidden;
    background: var(--stage);
  }
  .invitation {
    position: absolute;
    left: 170px;
    top: 150px;
    width: 860px;
    height: 600px;
    overflow: hidden;
    margin: 0;
  }
  .damask-field {
    position: absolute;
    inset: 0;
    background:
      radial-gradient(circle at 20% 30%, var(--damask) 0, transparent 60%),
      radial-gradient(circle at 80% 75%, var(--damask) 0, transparent 55%),
      var(--cream);
  }
  .ribbon {
    position: absolute;
    inset: 0;
  }
  .emblem-glow {
    position: absolute;
    left: 120px;
    top: 110px;
    width: 440px;
    height: 380px;
    border-radius: 50%;
    background: radial-gradient(ellipse at center,
      var(--glow) 0, var(--glow) 42%, rgba(255,255,255,0.85) 55%, rgba(255,255,255,0) 72%);
  }
  .couple-name {
    position: absolute;
    left: 120px;
    top: 270px;
    width: 440px;
    margin: 0;
    text-align: center;
    font-family: "Playball", cursive;
    font-weight: 400;
    font-size: 52px;
    line-height: 1;
    color: var(--plum);
  }
  .card-title {
    position: absolute;
    left: 620px;
    top: 500px;
    width: 200px;
    margin: 0;
    text-align: center;
    font-family: "Playball", cursive;
    font-weight: 400;
    color: var(--gold);
  }
  .card-title .headline {
    display: block;
    font-size: 38px;
    line-height: 1;
    letter-spacing: 2px;
  }
  .card-title .subline {
    display: block;
    font-size: 14px;
    line-height: 1;
    letter-spacing: 3px;
    margin-top: 4px;
  }
</style>
</head>
<body>
  <main class="invitation">
    <div class="damask-field" role="img" aria-label="Soft pink damask pattern on a cream ground"></div>
    <svg class="ribbon" viewBox="0 0 860 600" width="860" height="600" aria-hidden="true">
      <path class="ribbon-gold" fill="var(--gold)"
        d="M0,440 C320,330 540,140 860,0 L860,16 C540,156 320,346 0,458 Z"/>
      <path class="ribbon-magenta" fill="var(--magenta)"
        d="M0,458 C320,346 540,156 860,16 L860,34 C540,174 320,364 0,478 Z"/>
      <path class="ribbon-blush" fill="var(--blush)"
        d="M0,478 C320,364 540,174 860,34 L860,92 C600,160 300,390 40,600 L0,600 Z"/>
    </svg>
    <div class="emblem-glow"></div>
    <h2 class="couple-name">Amara &amp; Vikram</h2>
    <h1 class="card-title">
      <span class="headline">Wedding</span>
      <span class="subline">Invitation</span>
    </h1>
  </main>
</body>
</html>
```